KLV Messaging - veteran and exclusive boutique copywriting agency

PROJECT NEEDS:
1. Website design - full homepage design and inner page top banner design
2. Logo design
* Please see attached Briefs (Word Docs) for descriptions of what is needed for 1 and 2 above.
ABOUT THE CLIENT:
KLV Messaging is a veteran and exclusive boutique copywriting agency run by Marcus Holloway. Marcus is an award-winning published novelist and an accomplished executive ghostwriter with articles regularly published prominent technology publications like Brisk, ByteHarbor, FoundryPulse, and more. For nearly three decades, Marcus has focused solely on the technology sector - serving clients in Israel, Europe and the US.

Target Market(s)

hi-tech companies run by serious, confident professionals.

Industry/Entity Type

Business

Number of Pages Required

2 page

Font styles to use
Sans Serif
Other font styles liked:
• font should be modern

Colors
0054AA
0677BA
7BADD7
CADEEF
E8F1F8
F0912C
F2A743
F7CA91
FBE8D2
FDF5EE

Requirements
Must have
• psd files for logo, homepage design, and inner page top banner design
Nice to have
• Please see attached Website and Logo Design Briefs (Word Docs)
Should not have

```html
<!DOCTYPE html>
<html lang="en">
<head>
<meta charset="utf-8">
<title>KLV Messaging — The Words That Launch the Conversation</title>
<link href="https://fonts.googleapis.com/css2?family=Poppins:wght@300;400;500;600;700;800&display=swap" rel="stylesheet">
<style>
:root{
  --blue-deep:#0054AA;
  --blue:#0677BA;
  --blue-soft:#7BADD7;
  --orange:#F0912C;
  --orange-light:#F2A743;
  --ink:#1f2530;
  --text:#555b66;
  --dark:#2e2f33;
  --darker:#232427;
  --grey-bg:#f2f3f5;
  --line:#e3e5e9;
  --white:#ffffff;
  --ghost:rgba(120,125,135,.13);
}
*{box-sizing:border-box;margin:0;padding:0}
html,body{width:1200px;height:3124px;overflow:hidden}
body{font-family:'Poppins',sans-serif;color:var(--text);background:var(--white);position:relative}
.abs{position:absolute}
.ph{position:absolute}

/* hero */
.hero{left:0;top:0;width:1200px;height:700px;background:linear-gradient(100deg,#1b2433 0%,#2b3a4f 40%,#6d7f94 70%,#b7c2cf 100%)}
.hero-shade{left:0;top:0;width:1200px;height:700px;background:linear-gradient(90deg,rgba(10,16,28,.75) 0%,rgba(10,16,28,.35) 55%,rgba(10,16,28,0) 100%)}
.nav{left:0;top:0;width:1200px;height:72px;display:flex;align-items:center;justify-content:space-between;padding:0 60px}
.logo{font-weight:800;font-size:34px;color:var(--white);letter-spacing:1px;display:flex;align-items:center;gap:10px}
.logo-mark{width:12px;height:12px;background:var(--orange)}
.menu{display:flex;gap:26px;align-items:center;font-size:13px;color:var(--white)}
.hero-copy{left:60px;top:300px;width:560px;color:var(--white)}
.hero-title{font-weight:800;font-size:50px;line-height:1.08;text-transform:uppercase}
.hero-title span{color:var(--orange)}
.hero-lead{margin-top:20px;font-size:15px;line-height:1.6;color:#e6e9ee}
.hero-tag{left:60px;top:600px;font-size:14px;color:var(--white);line-height:1.6}
.hero-tag b{font-weight:600}
.dots{right:40px;top:330px;display:flex;flex-direction:column;gap:10px}
.dots i{display:block;width:8px;height:8px;border-radius:50%;background:rgba(255,255,255,.5)}
.dots i.on{background:var(--white)}

/* section heads */
.sec-title{font-weight:800;font-size:30px;color:var(--ink);text-transform:uppercase;line-height:1.1}
.sec-title::after{content:"";display:block;width:60px;height:4px;background:var(--orange);margin-top:10px}
.sec-title.center::after{margin:10px auto 0}
.ghost{left:0;width:1200px;text-align:center;font-weight:800;font-size:50px;line-height:60px;color:var(--ghost);text-transform:uppercase;white-space:nowrap;overflow:hidden}

/* about */
.about-copy{left:60px;top:728px;width:580px}
.about-copy p{font-size:12px;line-height:1.55;margin-top:5px}
.about-copy h4{font-size:13.5px;color:var(--ink);font-weight:700;margin-top:11px}
.about-copy .more{color:var(--orange);font-weight:600}
.about-img{left:672px;top:712px;width:408px;height:350px;background:linear-gradient(135deg,#e9ecf0,#c9d1da 60%,#8d98a5)}

/* services */
.services{left:0;top:1132px;width:1200px;height:318px;background:var(--orange)}
.services-title{left:0;top:1160px;width:1200px;text-align:center;color:var(--white);font-weight:800;font-size:28px;text-transform:uppercase}
.services-title::after{content:"";display:block;width:60px;height:4px;background:var(--white);margin:10px auto 0}
.card{top:1225px;width:300px;height:290px;background:var(--white);box-shadow:0 8px 24px rgba(0,0,0,.12)}
.card-img{width:300px;height:145px;background:linear-gradient(135deg,#cfd8e2,#8fa2b5)}
.card-body{padding:14px 18px}
.card-body h3{font-size:15px;font-weight:700;color:var(--ink)}
.card-body h5{font-size:11px;font-weight:600;color:var(--orange);margin-top:4px}
.card-body p{font-size:11.5px;line-height:1.55;margin-top:6px}

/* what we can do */
.wwd-img{left:120px;top:1600px;width:470px;height:330px;background:linear-gradient(135deg,#dde4ec,#9fb3c8 55%,#4d6784)}
.wwd-panel{left:560px;top:1620px;width:530px;height:310px;background:var(--white);box-shadow:0 8px 30px rgba(0,0,0,.12);padding:28px 32px}
.wwd-panel p{font-size:11.5px;line-height:1.55;margin-top:14px}
.wwd-list{margin-top:16px;display:grid;grid-template-columns:1fr 1fr;gap:8px 16px}
.wwd-item{display:flex;justify-content:space-between;align-items:center;border:1px solid var(--line);padding:6px 10px;font-size:11.5px;color:var(--ink)}
.chev{width:16px;height:16px}

/* why choose us */
.why{left:0;top:1980px;width:1200px;height:390px;background:var(--dark)}
.why-copy{left:60px;top:2030px;width:520px;color:#d7d9dd}
.why-copy .sec-title{color:var(--white)}
.why-copy p{font-size:12.5px;line-height:1.6;margin-top:18px}
.why-list{list-style:none;margin-top:18px}
.why-list li{display:flex;gap:12px;font-size:12.5px;line-height:1.5;margin-bottom:14px}
.why-list li::before{content:"";flex:none;width:10px;height:10px;border-radius:50%;background:var(--orange);margin-top:5px}
.why-img{left:672px;top:2010px;width:408px;height:330px;background:linear-gradient(135deg,#6f7a86,#3d4650 60%,#252b31)}

/* reviews */
.reviews{left:0;top:2400px;width:1200px;height:300px;background:var(--grey-bg)}
.rev-img{left:120px;top:2390px;width:410px;height:330px;background:linear-gradient(135deg,#e6ecf2,#aebfd0 55%,#6f8499)}
.rev-copy{left:600px;top:2430px;width:480px}
.rev-copy .sec-title{color:var(--blue-deep)}
.rev-copy blockquote{font-size:12.5px;line-height:1.6;margin-top:18px}
.rev-name{margin-top:18px;font-weight:700;font-size:12.5px;color:var(--ink);text-transform:uppercase}
.rev-role{font-size:11.5px}
.rev-dots{right:60px;top:2520px;display:flex;flex-direction:column;gap:10px}
.rev-dots i{display:block;width:8px;height:8px;border-radius:50%;background:#c3c7cd}
.rev-dots i.on{background:var(--ink)}

/* clients */
.clients-title{left:0;top:2800px;width:1200px;text-align:center}
.clients{left:110px;top:2890px;width:980px;display:flex;justify-content:space-between;align-items:center}
.client{display:flex;align-items:center;gap:8px;font-weight:700;font-size:20px;color:#3b3f46}
.client i{display:block;width:14px;height:14px;background:#9aa1ab}
.client-arrows{right:40px;top:2860px;display:flex;flex-direction:column;gap:6px}

/* footer */
.footer{left:0;top:2990px;width:1200px;height:134px;background:var(--darker);color:#b9bcc2}
.f-logo{left:60px;top:3008px;font-weight:800;font-size:30px;color:var(--white)}
.f-follow{left:60px;top:3060px;font-size:11.5px;color:var(--white)}
.f-social{left:60px;top:3082px;display:flex;gap:8px}
.f-social i{display:block;width:18px;height:18px;border-radius:50%;background:#5c6069}
.f-col{top:3010px;font-size:11.5px;line-height:1.7;color:#b9bcc2}
.f-col h6{font-size:12px;font-weight:600;color:var(--white);margin-bottom:2px}
.f-form{left:810px;top:3036px;display:flex}
.f-input{width:170px;height:30px;background:var(--white);font-size:11px;color:#8a8f98;padding:7px 10px}
.f-btn{width:60px;height:30px;background:var(--orange);color:var(--white);font-size:11px;font-weight:600;text-align:center;padding-top:7px}
.f-copy{left:810px;top:3080px;font-size:11px;color:#b9bcc2}
</style>
</head>
<body>

<!-- hero -->
<div class="ph hero" role="img" aria-label="Photo of a young girl working at a laptop in a bright office"></div>
<div class="abs hero-shade"></div>
<header class="abs nav">
  <div class="logo">KLV<i class="logo-mark"></i></div>
  <nav class="menu">
    <span>Home</span><span>About</span><span>Services</span><span>Industries</span><span>Portfolio</span><span>Clients</span><span>Contact</span>
    <svg width="16" height="16" viewBox="0 0 16 16" fill="none" stroke="#fff" stroke-width="2"><circle cx="7" cy="7" r="5"/><path d="M11 11l4 4"/></svg>
  </nav>
</header>
<div class="abs hero-copy">
  <h1 class="hero-title">The words that<br>launch the <span>conversation</span></h1>
  <p class="hero-lead">In a crowded marketplace, your messages need to engage. Your offering needs to rise above the background noise — but not by shouting.</p>
</div>
<p class="abs hero-tag">It's a conversation, not a speech.<br><b>It's the art of business communication.</b></p>
<div class="abs dots"><i class="on"></i><i></i><i></i></div>

<!-- about -->
<section class="abs about-copy">
  <h2 class="sec-title">About KLV</h2>
  <p>Based just north of Tel Aviv, KLV Messaging provides messaging, collateral creation, content marketing, and consulting to companies in Israel and abroad.</p>
  <h4>Messaging</h4>
  <p>Sometimes, it's good to step back. A fresh, outside view clarifies your perspective and focuses your marketing efforts where they will make the most impact. <span class="more">Learn More</span></p>
  <h4>Collateral &amp; Creative</h4>
  <p>From presentations, taglines and slogans to web content, data sheets and brochures — creative that speaks directly to your audience in the language they understand. <span class="more">Learn More</span></p>
  <h4>Content Marketing</h4>
  <p>We create marketable content in line with the positioning of your offering — content that moves your target audience to action. <span class="more">Learn More</span></p>
</section>
<div class="ph about-img" role="img" aria-label="Photo of a girl in glasses sitting at a desk"></div>

<div class="abs ghost" style="top:1070px">The art of business communication</div>

<!-- services -->
<div class="abs services"></div>
<h2 class="abs services-title">Our Services</h2>
<article class="abs card" style="left:120px">
  <div class="card-img" role="img" aria-label="Photo of a child reading with a parent"></div>
  <div class="card-body">
    <h3>Messaging</h3>
    <h5>The Value of Fresh Perspective</h5>
    <p>Focused market positioning that defines your value and shapes every message you send. <span style="color:var(--orange)">Learn More</span></p>
  </div>
</article>
<article class="abs card" style="left:450px">
  <div class="card-img" role="img" aria-label="Photo of a child writing at a desk"></div>
  <div class="card-body">
    <h3>Collateral</h3>
    <h5>Concise, Effective, Creative</h5>
    <p>Marketing collateral that effectively communicates who you are and what you want to say. <span style="color:var(--orange)">Learn More</span></p>
  </div>
</article>
<article class="abs card" style="left:780px">
  <div class="card-img" role="img" aria-label="Photo of children working together on laptops"></div>
  <div class="card-body">
    <h3>Content Marketing</h3>
    <h5>Giving Voice to Your Vision</h5>
    <p>Strong articles in the right places, in your voice, that build trust and expertise, not words. <span style="color:var(--orange)">Learn More</span></p>
  </div>
</article>

<div class="abs ghost" style="top:1524px">The art of business communication</div>

<!-- what we can do -->
<div class="ph wwd-img" role="img" aria-label="Photo of a boy presenting a chart"></div>
<section class="abs wwd-panel">
  <h2 class="sec-title">What we can do</h2>
  <p>Since 1995, KLV Messaging has had the opportunity to create collateral and content for tens of companies across a wide range of industries. Following is a small selection of recent projects.</p>
  <div class="wwd-list">
    <div class="wwd-item">Contributed Content<svg class="chev" viewBox="0 0 16 16"><circle cx="8" cy="8" r="8" fill="#F0912C"/><path d="M7 5l3 3-3 3" fill="none" stroke="#fff" stroke-width="1.6"/></svg></div>
    <div class="wwd-item">Web Site Content<svg class="chev" viewBox="0 0 16 16"><circle cx="8" cy="8" r="8" fill="#F0912C"/><path d="M7 5l3 3-3 3" fill="none" stroke="#fff" stroke-width="1.6"/></svg></div>
    <div class="wwd-item">Blog Content<svg class="chev" viewBox="0 0 16 16"><circle cx="8" cy="8" r="8" fill="#F0912C"/><path d="M7 5l3 3-3 3" fill="none" stroke="#fff" stroke-width="1.6"/></svg></div>
    <div class="wwd-item">Videos – Animated/Script<svg class="chev" viewBox="0 0 16 16"><circle cx="8" cy="8" r="8" fill="#F0912C"/><path d="M7 5l3 3-3 3" fill="none" stroke="#fff" stroke-width="1.6"/></svg></div>
    <div class="wwd-item">White Papers &amp; E-Books<svg class="chev" viewBox="0 0 16 16"><circle cx="8" cy="8" r="8" fill="#F0912C"/><path d="M7 5l3 3-3 3" fill="none" stroke="#fff" stroke-width="1.6"/></svg></div>
    <div class="wwd-item">Press Releases<svg class="chev" viewBox="0 0 16 16"><circle cx="8" cy="8" r="8" fill="#F0912C"/><path d="M7 5l3 3-3 3" fill="none" stroke="#fff" stroke-width="1.6"/></svg></div>
    <div class="wwd-item">Case Studies<svg class="chev" viewBox="0 0 16 16"><circle cx="8" cy="8" r="8" fill="#F0912C"/><path d="M7 5l3 3-3 3" fill="none" stroke="#fff" stroke-width="1.6"/></svg></div>
    <div class="wwd-item">Collateral<svg class="chev" viewBox="0 0 16 16"><circle cx="8" cy="8" r="8" fill="#F0912C"/><path d="M7 5l3 3-3 3" fill="none" stroke="#fff" stroke-width="1.6"/></svg></div>
  </div>
</section>

<!-- why choose us -->
<div class="abs why"></div>
<section class="abs why-copy">
  <h2 class="sec-title">Why choose us</h2>
  <p>Based just north of Tel Aviv, KLV Messaging provides messaging, collateral creation, content marketing and consulting to companies in Israel and abroad.</p>
  <ul class="why-list">
    <li>We know, on a level only few have, exactly how high tech works.</li>
    <li>Get confident to what traffic to your website — success is precisely where it should be.</li>
    <li>Enjoy a smoother, more innovative process with a personable team that delivers.</li>
  </ul>
</section>
<div class="ph why-img" role="img" aria-label="Photo of children in business attire standing in a group"></div>

<!-- reviews -->
<div class="abs reviews"></div>
<div class="ph rev-img" role="img" aria-label="Photo of children driving a small toy car"></div>
<section class="abs rev-copy">
  <h2 class="sec-title">Great reviews from<br>our clients</h2>
  <blockquote>Marcus quickly takes on whole companies, addressing the specific vision behind each project in a clear, thoughtful voice. His work is consistently strong, precise and effortless to read. Our launches have been far stronger thanks to him.</blockquote>
  <div class="rev-name">Daniel Ostrander</div>
  <div class="rev-role">Web Startup</div>
</section>
<div class="abs rev-dots"><i class="on"></i><i></i><i></i></div>

<div class="abs ghost" style="top:2700px">The art of business communication</div>

<!-- clients -->
<h2 class="abs sec-title center clients-title">Meet our clients</h2>
<div class="abs clients">
  <div class="client"><i></i>Brightwell</div>
  <div class="client"><i></i>Veranta</div>
  <div class="client"><i></i>Marqon</div>
  <div class="client"><i></i>Lumiqa</div>
  <div class="client"><i></i>Skyfold</div>
</div>
<div class="abs client-arrows">
  <svg width="14" height="10" viewBox="0 0 14 10"><path d="M1 9l6-7 6 7" fill="none" stroke="#1f2530" stroke-width="2"/></svg>
  <svg width="14" height="10" viewBox="0 0 14 10"><path d="M1 1l6 7 6-7" fill="none" stroke="#1f2530" stroke-width="2"/></svg>
</div>

<!-- footer -->
<footer class="abs footer"></footer>
<div class="abs f-logo">KLV</div>
<div class="abs f-follow">Follow us</div>
<div class="abs f-social"><i></i><i></i><i></i><i></i></div>
<div class="abs f-col" style="left:340px"><h6>About Us</h6>Contact<br>Features<br>Team<br>News</div>
<div class="abs f-col" style="left:560px"><h6>Resources</h6>Services<br>FAQs<br>Press Kit<br>Careers</div>
<div class="abs f-col" style="left:810px"><h6>Get Connect</h6></div>
<div class="abs f-form"><div class="f-input">Enter Email</div><div class="f-btn">Submit</div></div>
<div class="abs f-copy">Copyright © 2015–2022</div>

</body>
</html>
```